Packaging Design New Cosmetics Range

Small Establish online Beauty company is expanding it's product range into Serums, Sprays and Creams . We are looking for a new fresh packaging design for this launch.
We only use products that are Organic , Not Tested on Animals and Natural products
We would be interested in viewing a White Design , Black design and a designer choice of colors .
First Products are
Rose Water in 100ml glass bottle with box
and a set of 3 Face Serums Vit C , Retinol and Hyaluronic in 30ml Glass bottle = Box
Scrubs and creams will launch later in Q1 2020 however would like a similar feel across all products
Target Market(s)
SEA / US Markets
Industry/Entity Type
Cosmetics
Colors
Designer to choose colors to be used in the design.
Requirements
Must have
- Space Allocated for Product Use and Bar Codes on Box
Nice to have
- Organic , Not tested on animal Logo's

```html
<!DOCTYPE html>
<html lang="en">
<head>
<meta charset="utf-8">
<title>Velora Retinol &amp; Hyaluronic Serum Labels</title>
<link rel="stylesheet" href="https://fonts.googleapis.com/css2?family=Source+Sans+3:wght@300;400;600&family=PT+Sans+Narrow&display=swap">
<style>
  :root {
    --page-light: #f4f4f4;
    --page-dark: #8c8c8c;
    --label-ink: #0b0a12;
    --label-text: #ffffff;
    --rule: #000000;
    --purple-glow: #9a72cf;
    --purple-band: #a785d4;
    --purple-band-light: #c4a9e6;
    --pink-glow: #e0368a;
    --pink-band: #d9609b;
    --pink-band-light: #f59ac4;
    --blue-glow: #138bc0;
    --blue-band: #10a8e6;
    --blue-band-light: #4fd0ff;
  }
  * { box-sizing: border-box; margin: 0; padding: 0; }
  html, body { width: 1200px; height: 1200px; overflow: hidden; }
  body {
    background: radial-gradient(ellipse 70% 60% at 50% 62%, var(--page-light) 0%, #cfcfcf 55%, var(--page-dark) 100%);
    font-family: "Source Sans 3", sans-serif;
    position: relative;
  }
  .label-row {
    position: absolute;
    left: 60px; top: 380px;
    display: flex; gap: 30px;
  }
  .serum-label {
    position: relative;
    width: 340px; height: 440px;
    overflow: hidden;
    background: var(--label-ink);
    border-top: 14px solid var(--rule);
    color: var(--label-text);
  }
  .serum-label--retinol-purple { --glow: var(--purple-glow); --band: var(--purple-band); --band-light: var(--purple-band-light); }
  .serum-label--retinol-pink { --glow: var(--pink-glow); --band: var(--pink-band); --band-light: var(--pink-band-light); }
  .serum-label--retinol-blue { --glow: var(--blue-glow); --band: var(--blue-band); --band-light: var(--blue-band-light); }

  .light-beams {
    position: absolute; inset: 0;
    background:
      linear-gradient(90deg, transparent 0%, var(--glow) 30%, transparent 42%, var(--glow) 55%, transparent 68%, var(--glow) 85%, transparent 100%);
    opacity: .75;
    -webkit-mask-image: linear-gradient(180deg, #000 0%, rgba(0,0,0,.5) 35%, transparent 62%);
            mask-image: linear-gradient(180deg, #000 0%, rgba(0,0,0,.5) 35%, transparent 62%);
  }
  .center-glow {
    position: absolute; left: 70px; top: 110px; width: 200px; height: 120px;
    background: radial-gradient(ellipse at center, var(--glow) 0%, transparent 70%);
    opacity: .55;
  }
  .brand-mark {
    position: absolute; left: 50%; top: 0; transform: translateX(-50%);
    width: 88px; height: 98px;
    background: var(--label-ink);
    border: 2px solid var(--band-light);
    border-top: none;
    border-radius: 0 0 8px 8px;
    display: flex; flex-direction: column; align-items: center; justify-content: center; gap: 8px;
  }
  .brand-mark__dot { width: 18px; height: 18px; border-radius: 50%; border: 2px solid var(--label-text); }
  .brand-mark__name { font-size: 22px; font-weight: 400; color: var(--label-text); line-height: 1; }

  .directions {
    position: absolute; left: 4px; top: 292px;
    transform: rotate(-90deg); transform-origin: left top;
    font-size: 7px; line-height: 10px; width: 250px; opacity: .85;
  }
  .serum-facts {
    position: absolute; left: 300px; top: 56px; width: 80px; height: 240px;
    border: 1px solid var(--label-text);
    padding: 4px 5px; font-size: 8px; line-height: 12px;
  }
  .serum-facts__title { font-weight: 600; font-size: 11px; }
  .serum-facts__rule { border-top: 3px solid var(--label-text); margin: 4px 0; }
  .serum-facts__line { border-top: 1px solid var(--label-text); }

  .product-name {
    position: absolute; left: 40px; top: 238px;
    font-size: 45px; font-weight: 400; line-height: 42px; letter-spacing: -.5px;
  }
  .product-type {
    position: absolute; left: 40px; top: 326px; width: 236px;
    border-top: 1px solid var(--label-text);
    padding-top: 4px;
    font-size: 16px; text-align: center; letter-spacing: .2px;
  }
  .volume-band {
    position: absolute; left: 0; right: 0; top: 352px; height: 38px;
    background: linear-gradient(180deg, var(--band-light) 0%, var(--band) 100%);
    border-top: 3px solid var(--band-light);
    font-family: "PT Sans Narrow", sans-serif;
    font-size: 24px; line-height: 34px; text-align: center;
  }
  .label-foot {
    position: absolute; left: 0; right: 0; top: 390px; bottom: 0;
    background: #1a0f0c;
  }
</style>
</head>
<body>
  <main class="label-row">
    <section class="serum-label serum-label--retinol-purple">
      <div class="light-beams"></div>
      <div class="center-glow"></div>
      <div class="brand-mark"><span class="brand-mark__dot"></span><span class="brand-mark__name">Velora</span></div>
      <p class="directions">Consult a doctor about allergies or other possible complications before using this product.<br>DIRECTIONS: Take 0.6 mL (approx. 24 drops) twice per day.</p>
      <div class="serum-facts">
        <div class="serum-facts__title">Serum Facts</div>
        Serving 0.6 mL<br>(approx. 24 drops)<br>Servings 50
        <div class="serum-facts__rule"></div>
        <div class="serum-facts__line">Calories 0</div><div class="serum-facts__line">Carbs 0g</div><div class="serum-facts__line">Total 0g</div>
        <div class="serum-facts__rule"></div>
        Phenoxy 1%<br>Hexyl 1%<div class="serum-facts__line">*Percent based<br>**Daily value</div>
      </div>
      <h1 class="product-name">Retinol &amp;<br>Hyaluronic</h1>
      <p class="product-type">MOISTURIZING SERUM</p>
      <p class="volume-band">1 fl/oz&nbsp; (30 ml)</p>
      <div class="label-foot"></div>
    </section>

    <section class="serum-label serum-label--retinol-pink">
      <div class="light-beams"></div>
      <div class="center-glow"></div>
      <div class="brand-mark"><span class="brand-mark__dot"></span><span class="brand-mark__name">Velora</span></div>
      <p class="directions">Consult a doctor about allergies or other possible complications before using this product.<br>DIRECTIONS: Take 0.6 mL (approx. 24 drops) twice per day.</p>
      <div class="serum-facts">
        <div class="serum-facts__title">Serum Facts</div>
        Serving 0.6 mL<br>(approx. 24 drops)<br>Servings 50
        <div class="serum-facts__rule"></div>
        <div class="serum-facts__line">Calories 0</div><div class="serum-facts__line">Carbs 0g</div><div class="serum-facts__line">Total 0g</div>
        <div class="serum-facts__rule"></div>
        Phenoxy 1%<br>Hexyl 1%<div class="serum-facts__line">*Percent based<br>**Daily value</div>
      </div>
      <h2 class="product-name">Retinol &amp;<br>Hyaluronic</h2>
      <p class="product-type">MOISTURIZING SERUM</p>
      <p class="volume-band">1 fl/oz&nbsp; (30 ml)</p>
      <div class="label-foot"></div>
    </section>

    <section class="serum-label serum-label--retinol-blue">
      <div class="light-beams"></div>
      <div class="center-glow"></div>
      <div class="brand-mark"><span class="brand-mark__dot"></span><span class="brand-mark__name">Velora</span></div>
      <p class="directions">Consult a doctor about allergies or other possible complications before using this product.<br>DIRECTIONS: Take 0.6 mL (approx. 24 drops) twice per day.</p>
      <div class="serum-facts">
        <div class="serum-facts__title">Serum Facts</div>
        Serving 0.6 mL<br>(approx. 24 drops)<br>Servings 50
        <div class="serum-facts__rule"></div>
        <div class="serum-facts__line">Calories 0</div><div class="serum-facts__line">Carbs 0g</div><div class="serum-facts__line">Total 0g</div>
        <div class="serum-facts__rule"></div>
        Phenoxy 1%<br>Hexyl 1%<div class="serum-facts__line">*Percent based<br>**Daily value</div>
      </div>
      <h2 class="product-name">Retinol &amp;<br>Hyaluronic</h2>
      <p class="product-type">MOISTURIZING SERUM</p>
      <p class="volume-band">1 fl/oz&nbsp; (30 ml)</p>
      <div class="label-foot"></div>
    </section>
  </main>
</body>
</html>
```